Design eBook cover and interior pages for vegan investment consulting firm and membership service...

I have completed an eBook that is about 6 pages of printed text (see attached PDF). I am seeking a cover page and a cool design for the interior pages. The final product should be as concise as possible while being easy to read, and not to exceed 10 pages total in any case.

My business is named Plantwise Harbor. You can learn more about the company by visiting https://plantwiseharbor.example. There, you’ll also see our current color and design choices.

We are about to start a Phase II redesign of the website, so it is not required that you match the color and style of our website. I am open to any fresh ideas regarding color, fonts, and overall aesthetic that might also inform our website redesign.

The business serves individuals “investor members” who have $50,000 or more in their investment portfolio, and also provides “purpose driven” portfolio design consulting to endowments, large asset managers, and high net worth individuals who are looking to build a vegan portfolio over $10 million or more.

Because we’re dealing with investing and people’s life savings, we want the eBook look to convey responsibility and integrity. At the same time, our audience will participate because of they are also passionate about all things vegan - protecting animals, the environment, and human health. To summarize, the goal is to have an eBook design that conveys a blend of responsibility, integrity, and passion.

Note - there is a tendency for people to first think of the color green when designing for vegan enterprises. I feel that using green as a major and even as a minor color often creates difficult or weak design outcomes. Green has become a kind of design shorthand for all things vegan and environmental, and as a result, I feel it has lost any special meaning.

Since we provide serious services to people who take investing seriously, I want color and design styles that read well, and convey responsibility, integrity and passion without relying on overused design cliches, but while still conveying a fresh perspective.

```html
<!DOCTYPE html>
<html lang="en">
<head>
<meta charset="utf-8">
<title>5 Vegan Businesses You Should Be Investing In Today — eBook spreads</title>
<link href="https://fonts.googleapis.com/css2?family=Oswald:wght@500;700&family=Open+Sans:wght@400;600;700&display=swap" rel="stylesheet">
<style>
  :root {
    --canvas: #ffffff;
    --paper: #ffffff;
    --page-edge: #d9d9d9;
    --ink: #2b2b2b;
    --ink-soft: #6b6b6b;
    --accent: #8e1b1f;
    --soil-dark: #3d2f24;
    --soil-mid: #7a6450;
    --rule: #bdbdbd;
    --table-head: #f1f1f1;
  }
  * { margin: 0; padding: 0; box-sizing: border-box; }
  html, body { width: 1200px; height: 473px; overflow: hidden; background: var(--canvas); }
  body { position: relative; font-family: "Open Sans", Arial, sans-serif; color: var(--ink); }

  .page-row { position: absolute; display: flex; gap: 8px; }
  .page-row--top { top: 3px; left: 2px; }
  .page-row--bottom { top: 243px; left: 88px; }

  .page {
    position: relative; width: 164px; height: 227px; background: var(--paper);
    border: 1px solid var(--page-edge); box-shadow: 0 1px 3px rgba(0,0,0,.18);
    padding: 18px 14px 16px; overflow: hidden;
  }
  .page__title {
    font-family: "Oswald", "Arial Narrow", sans-serif; font-weight: 700; font-size: 8.2px;
    text-align: center; text-transform: uppercase; line-height: 1.25; margin: 4px 0 8px; color: var(--ink);
  }
  .page__subhead { font-weight: 700; font-size: 3.4px; text-transform: uppercase; margin: 4px 0 2px; }
  .body-text { font-size: 3.3px; line-height: 1.55; margin-bottom: 3.2px; color: var(--ink); }
  .body-text--list { padding-left: 5px; }
  .drop { font-size: 7px; font-weight: 700; float: left; line-height: 1; margin-right: 1px; color: var(--accent); }

  .page__footer {
    position: absolute; bottom: 7px; left: 14px; right: 14px; font-size: 3px; letter-spacing: .2px;
    color: var(--ink-soft); text-transform: uppercase; border-top: 0.5px solid var(--rule); padding-top: 2px;
  }
  .page__footer--right { text-align: right; }
  .page__footer b { color: var(--accent); font-weight: 700; }

  /* cover */
  .cover { padding: 0; border-color: #cfcfcf; }
  .cover__title {
    position: absolute; top: 12px; left: 10px; right: 10px; text-align: center;
    font-family: "Oswald", "Arial Narrow", sans-serif; font-weight: 700; color: var(--accent);
    font-size: 15.5px; line-height: 1.08; text-transform: uppercase;
  }
  .cover__image {
    position: absolute; top: 78px; left: 0; right: 0; bottom: 0;
    background: linear-gradient(180deg, #ffffff 0%, #f2ede7 35%, #b7a48f 62%, var(--soil-mid) 78%, var(--soil-dark) 100%);
  }
  .cover__author {
    position: absolute; bottom: 10px; left: 0; right: 0; text-align: center; color: #ffffff;
    font-family: "Oswald", "Arial Narrow", sans-serif; font-weight: 500; font-size: 11px;
  }

  /* about */
  .author-photo { float: left; width: 26px; height: 28px; margin: 1px 4px 2px 0; background: linear-gradient(160deg, #b9b2a8, #6f665c); }
  .signature { width: 50px; height: 16px; margin: 6px 0 0; background: linear-gradient(90deg, #c9c3d8, #8d85ad); opacity: .7; border-radius: 2px; }

  /* tables */
  .data-table { width: 78%; margin: 5px auto 6px; border-collapse: collapse; font-size: 3px; }
  .data-table th, .data-table td { border: 0.5px solid #9a9a9a; padding: 1.6px 2px; text-align: left; }
  .data-table th { background: var(--table-head); font-weight: 700; text-align: center; }
  .data-table td.num { text-align: right; }
  .data-table--compare { width: 100%; margin: 2px 0 5px; }
  .data-table--compare td.mark { text-align: center; color: var(--accent); font-weight: 700; }
  .table-caption { font-size: 3.3px; font-weight: 700; text-transform: uppercase; margin-top: 0; }
</style>
</head>
<body>

<section class="page-row page-row--top">
  <article class="page cover">
    <h1 class="cover__title">5 Vegan Businesses You Should Be Investing In Today</h1>
    <div class="cover__image" role="img" aria-label="Photo of a hand holding dark soil with a young green sprout"></div>
    <p class="cover__author">Dana Whitcombe</p>
  </article>

  <article class="page">
    <p class="page__footer">2 | 5 Vegan Businesses You Should Be Investing In Today</p>
  </article>

  <article class="page">
    <h2 class="page__title">Meet Dana Whitcombe</h2>
    <p class="page__subhead">Founder, Plantwise Harbor</p>
    <div class="author-photo" role="img" aria-label="Portrait photo of the author"></div>
    <p class="body-text">Throughout my adult life, I have worked to solve difficult ecological, social and health challenges with creative business, financial and social engineering strategies.</p>
    <p class="body-text">I started my first purpose driven environmental business in 1985 and by 1990 became one of the youngest environmental service directors in the region.</p>
    <p class="body-text">These experiences solidified my belief that purpose driven businesses can be built to solve big challenges in ways that are not possible via charities, NGOs and governments alone.</p>
    <p class="body-text">Not only can purpose driven businesses ideally solve today’s challenges, it is clear to me that they are and should be highly profitable due to the vast and profitable market opportunities available for transforming our economy.</p>
    <p class="body-text">To fulfil this vision, I had to learn one of the most challenging and misunderstood fields in the world — corporate finance. In 2001 I left direct entrepreneurship and leadership to gain the financial experience needed to design, fund and grow purpose driven businesses that scale.</p>
    <p class="page__footer page__footer--right">Dana Whitcombe | <b>3</b></p>
  </article>

  <article class="page">
    <p class="body-text">Business people from growth to IPO a wide range of meaningful market opportunities in media, the world’s leading plant-based food and consumer brands.</p>
    <p class="body-text">At Plantwise Harbor, with investment growth, investor members will have increasing opportunities to work together and grow the vegan economy for the benefit of the animals, human health and the environment. I look forward to sharing this journey with you!</p>
    <p class="body-text">Sincerely,</p>
    <div class="signature" role="img" aria-label="Handwritten signature of the author"></div>
    <p class="page__footer">4 | 5 Vegan Businesses You Should Be Investing In Today</p>
  </article>

  <article class="page">
    <h2 class="page__title">How Big Is the Vegan Economy Today?</h2>
    <p class="body-text"><span class="drop">T</span>he vegan movement has been growing by leaps and bounds. Today there are an estimated 20 million U.S. vegans, an increase of over 500% since 2014. Market growth is occurring in nearly every consumer sector.</p>
    <p class="body-text">The U.S. Bureau of Labor Statistics reports that in 2017 the average U.S. consumer spent $60,060. Two major categories represent the immediate opportunities for growth in the vegan sector: food eaten at home, food eaten at restaurants, apparel, health care and personal care products.</p>
    <p class="body-text">The table shows how much today’s U.S. vegans are currently spending annually in each of these sectors:</p>
    <table class="data-table">
      <thead><tr><th>Category</th><th>20 Million U.S. Vegan Consumers<br>Total Annual Spending Per Category</th></tr></thead>
      <tbody>
        <tr><td>Food at home</td><td class="num">$87 billion</td></tr>
        <tr><td>Food at restaurants</td><td class="num">$61 billion</td></tr>
        <tr><td>Apparel</td><td class="num">$37 billion</td></tr>
        <tr><td>Health Care</td><td class="num">$96 billion</td></tr>
        <tr><td>Personal Care Products</td><td class="num">$19 billion</td></tr>
        <tr><td><b>Total</b></td><td class="num"><b>$300 billion</b></td></tr>
      </tbody>
    </table>
    <p class="page__footer page__footer--right">Dana Whitcombe | <b>5</b></p>
  </article>

  <article class="page">
    <p class="body-text">The above table shows that demand for clearly labeled vegan products is huge. To ensure this existing vegan market remains strong, simply need to ensure that no animals were harmed in the making of the products, and that such products are positioned as vegan friendly.</p>
    <p class="page__footer">6 | 5 Vegan Businesses You Should Be Investing In Today</p>
  </article>

  <article class="page">
    <h2 class="page__title">Leading Vegan Investment Opportunities Today</h2>
    <p class="body-text"><span class="drop">T</span>wo major contributors to the growth of vegan products are adding demand by the large increase in existing vegans, and a major shift in mainstream consumer groups towards plant based eating.</p>
    <p class="body-text">Let’s look more closely at how this growth in vegan commitment is building businesses and creating investment opportunities in these five market segments.</p>
    <p class="page__subhead">1. Vegan Convenience Food</p>
    <p class="body-text">Vegan substitutes for meat, dairy and eggs are growing dramatically. Now there are products that replace almost every animal-based item in the grocery aisle. This presents an exceptional investment opportunity as more people want to eat conveniently and meet vegan expectations.</p>
    <p class="page__subhead">2. Vegan Restaurants</p>
    <p class="body-text">It is nearly impossible to find a nutritious and fulfilling vegan meal at most fast food restaurant chains. Yet, vegans alone account for $27 billion of the total U.S. annual restaurant market, a number projected to exceed $40 billion.</p>
    <p class="body-text">Emerging vegan fast food brands have shown how well plant-based menus perform at scale and attract a growing audience.</p>
    <p class="page__footer page__footer--right">Dana Whitcombe | <b>7</b></p>
  </article>
</section>

<section class="page-row page-row--bottom">
  <article class="page">
    <p class="body-text">Fast food chains are only one slice of the growing vegan food service industry. There are even more investment opportunities to transform sources of catering, corporate dining and institutional food providers such as schools, hospitals, corporate cafeterias, military bases and more.</p>
    <p class="page__subhead">3. Vegan Apparel and Lifestyle Products</p>
    <p class="body-text">Veganism is much more than a diet. It is a lifestyle embracing a commitment to compassion and fundamental rights for animals.</p>
    <p class="body-text">Today, animal materials are used in all sorts of apparel, whether it is the obvious leather or fur, or less discernible animal-based adhesives. With today’s technology, there is no longer any reason for animals to be used in sourcing of industrial endeavors.</p>
    <p class="body-text">U.S. leather consumption points to the size of this opportunity. U.S. leather clothing is $10 billion annually, not including leather accessories that otherwise feature a consumer gain.</p>
    <p class="body-text">Material technology companies are innovating alternatives to animal skins and glues in consumer and industrial products. Emerging brands are producing visually rich footwear, accessories and fashion items that consumers value.</p>
    <p class="body-text">In 2017, membership grew in niche vegan apparel retail. The trend shows that new high-end plant based fashion brands find consumers willing to pay for quality and ethics alike.</p>
    <p class="page__footer">8 | 5 Vegan Businesses You Should Be Investing In Today</p>
  </article>

  <article class="page">
    <p class="page__subhead">4. Vegan Health and Lifestyle Medicine</p>
    <p class="body-text">Nearly 100 years of clinical research has demonstrated that most chronic illnesses found in western nations are increasingly food related and can be reversed or slowed with healthy whole-food plant-based diets.</p>
    <p class="body-text">One of the most widely respected illnesses types is diabetes, which affects over 30 million Americans and more than seven in ten associated with consumption and management expenses.</p>
    <p class="body-text">Recent reviews show that diet-based intervention for diabetes, arthritis and many other chronic illnesses can be greatly improved. Including many doctors support creation of plant-based lifestyle centers.</p>
    <p class="body-text">Over the past 20 years, a growing number of MDs have established plant based medical clinics and corporate wellness programs using diet to reduce weight, restore health and end dependence on drug based treatments. With U.S. healthcare expenditure topping $3 trillion annually, high growth opportunities exist in lifestyle medicine.</p>
    <p class="body-text">Plant based MDs cite direct evidence to treat the causes of chronic illness from eating a plant based diet. This means insurers and employers are seeking partners to deliver these benefits.</p>
    <p class="page__subhead">5. Personal Care Products</p>
    <p class="body-text">The U.S. personal care products market is valued at over $56 billion. Vegan and cruelty-free brands are gaining share as new consumers demand transparency and ethical sourcing.</p>
    <p class="page__footer page__footer--right">Dana Whitcombe | <b>9</b></p>
  </article>

  <article class="page">
    <p class="body-text">Excellent growth opportunities exist for new brands. Now that regulation is helping certify and label, vegan brands that cultivate trust and clear ingredients will capture durable market share from legacy manufacturers for cosmetics, skincare and household needs.</p>
    <p class="page__footer">10 | 5 Vegan Businesses You Should Be Investing In Today</p>
  </article>

  <article class="page">
    <h2 class="page__title">How Can I Invest in the Vegan Economy?</h2>
    <p class="body-text"><span class="drop">F</span>irst, if any vegan enterprises provide publicly traded stock. For the most part, investing in the vegan economy requires investing in “private offers”. Private offers are government regulated contracts offering companies that do not trade publicly to raise capital from a small number of potential investors through exempt transactions.</p>
    <p class="body-text">To successfully invest in private offers, one must be able to find offers, be legally qualified to invest, and thoroughly understand the risks.</p>
    <p class="page__subhead">The Do-It-Yourself Approach</p>
    <p class="body-text body-text--list">1. You must first locate startups on your own: join networks in your vegan community and online, and be prepared to meet founders with your own due diligence and patience.</p>
    <p class="body-text body-text--list">2. You will need to qualify as an accredited investor in most cases, with an income over $200,000 or net worth over $1 million excluding your home.</p>
    <p class="body-text body-text--list">3. Crowdfunding platforms and online portals can connect early stage investors with vegan offerings, but terms vary greatly and most lack ongoing support.</p>
    <p class="page__footer page__footer--right">Dana Whitcombe | <b>11</b></p>
  </article>

  <article class="page">
    <p class="body-text body-text--list">4. Your diversification will not be much help. Most founders carefully do not have the proper training to present private offers to their clients. In addition, most brokerage firms prohibit their brokers from offering them for financial products they are not publicly traded.</p>
    <p class="page__subhead">The Investor Member Approach</p>
    <p class="body-text">As you can see, despite the obvious growth in the vegan market, vegan investments are extremely challenging to find, time consuming to research, and risky to manage alone.</p>
    <p class="body-text">At Plantwise Harbor, we make investing in the vegan market remarkably easy.</p>
    <p class="body-text">Plantwise Harbor provides a steady flow of private investment opportunities in the rapid growing vegan market to both accredited and non-accredited investor members.</p>
    <p class="page__footer">12 | 5 Vegan Businesses You Should Be Investing In Today</p>
  </article>

  <article class="page">
    <p class="table-caption">Plantwise Harbor Member Benefits</p>
    <table class="data-table data-table--compare">
      <thead><tr><th>Benefit</th><th>Non-accredited Investors</th><th>Accredited Investors</th></tr></thead>
      <tbody>
        <tr><td>Steady flow of vegan investment opportunities</td><td class="mark">yes</td><td class="mark">yes</td></tr>
        <tr><td>Expertly vetted private market opportunities</td><td class="mark">yes</td><td class="mark">yes</td></tr>
        <tr><td>Due diligence reports on each opportunity</td><td class="mark">yes</td><td class="mark">yes</td></tr>
        <tr><td>Opportunity to invest together in a coordinated way with other vegan investors</td><td class="mark">yes</td><td class="mark">yes</td></tr>
        <tr><td>Semi-annual private online meetings to review your vegan investment portfolio and more</td><td class="mark">yes</td><td class="mark">yes</td></tr>
        <tr><td>Consult with our professional wealth management advisors, accountants, and attorneys to plan secure investment suitability</td><td></td><td class="mark">yes</td></tr>
        <tr><td>Gain access to accredited-only offers and private placements with our most qualified partners</td><td></td><td class="mark">yes</td></tr>
      </tbody>
    </table>
    <p class="body-text"><b>Note:</b> Custom portfolio design consulting services are available for individuals and investment funds wishing to allocate $10 million or more to the vegan investment market.</p>
    <p class="page__footer page__footer--right">Dana Whitcombe | <b>13</b></p>
  </article>
</section>

</body>
</html>
```